Quendra - Clear Spirit Cosmetics

Please design a logo and business cards for new food supplements, cosmetics and herbal fixatives. The products are produced ecologically and biologically in the South Tyrol and Trentino alps. The products are pure and noble. Quendra = pure vitality Colors Background: dark or black matt (soft touch) Logodesign: powerful, elegant, violet with glossy foil The logo and design should convey warmth, passion and the 6th sense, you should get the impression that you can smell the herbal odor , Logo and business cards for new food supplements, cosmetics and herbal fixatives. The products are produced ecologically and biologically in the South Tyrol and Trentino alps. The products are pure and noble. Quendra = pure vitality Colors Background: dark or black matt (softtouch) Logodesign: powerful elegant violet with glossy foil The logo and design is meant to convey warmth, passion and the 6th sense, you should get the impression that you can smell the herbal perfume.

Target Market(s)

Food, food supplements, vitality, health

Contact Information for Business Card

Please provide an elegant darf design that is puristic, but has a very good logo design
Elegantes dunkles design, puristisch

Logo Text

Quendra - clear Spirit

Colors
6b449b

Requirements
Must have
• SVG Files Alpha channel for foil embossing High-quality design
Nice to have
• Pure elegance
Should not have
• to colorful colors

```html
<!DOCTYPE html>
<html lang="en">
<head>
<meta charset="utf-8">
<title>Quendra – Business Card</title>
<link rel="stylesheet" href="https://fonts.googleapis.com/css2?family=Inter:wght@300;400;600&display=swap">
<style>
  :root {
    --backdrop: #8b8c8b;
    --card: #2a2a2a;
    --violet: #7b3fb3;
    --text-strong: #dcdcdc;
    --text-soft: #a3a3a3;
    --rule: #8a8a8a;
  }
  html, body {
    margin: 0;
    padding: 0;
    overflow: hidden;
  }
  body {
    width: 1200px;
    height: 1038px;
    background: var(--backdrop);
    position: relative;
    font-family: "Inter", Helvetica, Arial, sans-serif;
  }
  .business-card {
    position: absolute;
    left: 442px;
    top: 249px;
    width: 333px;
    height: 600px;
    background: var(--card);
    border-radius: 13px;
    text-align: center;
  }
  .holder {
    position: absolute;
    top: 63px;
    left: 0;
    right: 0;
  }
  .holder-name {
    margin: 0;
    font-size: 18px;
    font-weight: 400;
    letter-spacing: 0.2px;
    color: var(--text-strong);
    line-height: 1.2;
  }
  .holder-role {
    margin: 4px 0 0;
    font-size: 13px;
    font-weight: 300;
    color: var(--text-strong);
  }
  .brand {
    position: absolute;
    top: 205px;
    left: 0;
    right: 0;
  }
  .brand-mark {
    display: block;
    margin: 0 auto 14px;
  }
  .brand-name {
    margin: 0;
    font-size: 30px;
    font-weight: 600;
    letter-spacing: 1px;
    color: var(--violet);
    line-height: 1;
  }
  .contact {
    position: absolute;
    top: 416px;
    left: 0;
    right: 0;
    font-size: 13px;
    font-weight: 300;
    color: var(--text-soft);
    line-height: 17px;
  }
  .contact p { margin: 0; }
  .contact-rule {
    width: 32px;
    height: 1px;
    background: var(--rule);
    margin: 16px auto 17px;
  }
</style>
</head>
<body>
  <section class="business-card">
    <header class="holder">
      <h1 class="holder-name">MARA VELDEN</h1>
      <p class="holder-role">General Manager</p>
    </header>

    <div class="brand">
      <svg class="brand-mark" width="44" height="44" viewBox="0 0 44 44" aria-hidden="true">
        <circle cx="22" cy="22" r="20" fill="var(--violet)"/>
      </svg>
      <p class="brand-name">QUENDRA</p>
    </div>

    <address class="contact">
      <p>+43 660 48213075</p>
      <p>info@quendra.com</p>
      <p>www.quendra.com</p>
      <div class="contact-rule"></div>
      <p>Lindenstraße 12</p>
      <p>4650 Steinhaus</p>
    </address>
  </section>
</body>
</html>
```